Wanted: A Simple yet Awesome Blog Hero Image

We need a hero image (blog graphic header) to replace our existing one: https://www.terravexlab.com//blog/soil-classification-foundation-and-pavement-design-starts-here
Want something to reflect what the blog article is about and is a reflection of the title.

Note: we are not in love with any of our hero graphics

Industry/Entity Type

Construction

Colors

Designer to choose colors to be used in the design.

Requirements
Must have
• Width must be 715px
• Height must not exceed 400px
• Content on graphic should be: Soil Classification: Foundation and Pavement Design Starts Here
Nice to have
• a product shown that is mentioned in the blog
Should not have
• a product with a Carrowmere logo

```html
<!DOCTYPE html>
<html lang="en">
<head>
<meta charset="UTF-8">
<title>Soil Classification: Foundation and Pavement Design Starts Here</title>
<link href="https://fonts.googleapis.com/css2?family=Anton&family=Roboto:ital,wght@1,700&display=swap" rel="stylesheet">
<style>
  :root {
    --page-bg: #ffffff;
    --soil-dark: #1f150e;
    --soil-mid: #3b2a1d;
    --soil-light: #5a4330;
    --headline-top: #ffffff;
    --headline-bottom: #bdbdbd;
    --accent-orange: #f7a11a;
    --accent-red: #e8312a;
    --shadow: rgba(0, 0, 0, 0.85);
  }
  * { margin: 0; padding: 0; box-sizing: border-box; }
  html, body {
    width: 1200px;
    height: 1200px;
    overflow: hidden;
    background: var(--page-bg);
  }
  .variant {
    position: absolute;
    left: 123px;
    width: 953px;
    height: 533px;
    overflow: hidden;
    background:
      radial-gradient(ellipse at 40% 45%, var(--soil-light) 0%, var(--soil-mid) 45%, var(--soil-dark) 100%);
  }
  .variant--orange { top: 53px; }
  .variant--red { top: 613px; }

  .product-photo {
    position: absolute;
    left: 371px;
    top: 4px;
    width: 560px;
    height: 252px;
    border-radius: 6px;
    background: linear-gradient(120deg, #d9d4c8 0%, #b8b2a6 35%, #c8352b 55%, #9a9a9a 80%, #d0d3da 100%);
    opacity: 0.9;
  }
  .hand-photo {
    position: absolute;
    left: 0;
    top: 320px;
    width: 357px;
    height: 213px;
    background: linear-gradient(90deg, #7a5a44 0%, #5b4130 55%, rgba(59, 42, 29, 0) 100%);
  }

  .headline {
    position: absolute;
    font-family: "Anton", "Impact", sans-serif;
    line-height: 1;
    text-transform: uppercase;
    background: linear-gradient(180deg, var(--headline-top) 0%, var(--headline-top) 45%, var(--headline-bottom) 100%);
    -webkit-background-clip: text;
    background-clip: text;
    color: transparent;
    filter: drop-shadow(3px 4px 4px var(--shadow));
    white-space: nowrap;
  }
  .headline--soil {
    left: 64px;
    top: 60px;
    font-size: 170px;
  }
  .headline--classification {
    left: 86px;
    top: 238px;
    font-size: 138px;
  }

  .tagline {
    position: absolute;
    right: 56px;
    top: 402px;
    font-family: "Roboto", "Arial", sans-serif;
    font-style: italic;
    font-weight: 700;
    font-size: 31px;
    line-height: 43px;
    text-align: right;
    text-transform: uppercase;
    text-shadow: 2px 2px 3px var(--shadow);
    white-space: nowrap;
  }
  .variant--orange .tagline { color: var(--accent-orange); }
  .variant--red .tagline { color: var(--accent-red); }
</style>
</head>
<body>
  <section class="variant variant--orange" role="img" aria-label="Close-up photograph of dark brown soil filling the background">
    <div class="product-photo" role="img" aria-label="Soil classification kit: red toolbox, soil colour charts, sieves and testing tools"></div>
    <div class="hand-photo" role="img" aria-label="Hands holding a mound of loose soil"></div>
    <h1 class="headline headline--soil">Soil</h1>
    <p class="headline headline--classification">Classification:</p>
    <p class="tagline">Foundation and pavement<br>design starts here</p>
  </section>

  <section class="variant variant--red" role="img" aria-label="Close-up photograph of dark brown soil filling the background">
    <div class="product-photo" role="img" aria-label="Soil classification kit: red toolbox, soil colour charts, sieves and testing tools"></div>
    <div class="hand-photo" role="img" aria-label="Hands holding a mound of loose soil"></div>
    <p class="headline headline--soil">Soil</p>
    <p class="headline headline--classification">Classification:</p>
    <p class="tagline">Foundation and pavement<br>design starts here</p>
  </section>
</body>
</html>
```